Commercial Office Fitout company needs a simple website

We need a website for our company Tallow Bridge (QLD) Pty Ltd. We are in the construction industry and we specialise in commercial office fitouts (partitions/glass/doors). Our company colours are black and silver. Please use our logo attached.
We only need an "about us" section, a "portfolio" section where we display some pictures of our work, and a "contact us" section. We would like our website to be simple, effective, professional and modern.

Industry/Entity Type

Construction

Number of Pages Required

1 page

```html
<!DOCTYPE html>
<html lang="en">
<head>
<meta charset="utf-8">
<title>Tallow Bridge (QLD) Pty Ltd – Contact</title>
<link href="https://fonts.googleapis.com/css2?family=Raleway:wght@300;400;500;700&display=swap" rel="stylesheet">
<style>
  :root {
    --page-bg: #ffffff;
    --band-bg: #f8f8f8;
    --ink: #2a2a2a;
    --ink-soft: #555b66;
    --muted: #777b80;
    --button: #262626;
    --field-line: #b9b9b9;
    --map-base: #e3e3e3;
    --map-edge: #d8d8d8;
    --pin: #e8615f;
    --footer: #535a66;
    --footer-ink: #ffffff;
    --photo-a: #3e3328;
    --photo-b: #e6d4bf;
    --photo-c: #55585e;
  }
  * { box-sizing: border-box; margin: 0; padding: 0; }
  html, body { width: 1200px; height: 1200px; overflow: hidden; }
  body { position: relative; background: var(--page-bg); font-family: "Raleway", sans-serif; color: var(--ink); }

  .portfolio-band { position: absolute; left: 0; top: 0; width: 1200px; height: 182px; background: var(--band-bg); }
  .portfolio-photo { position: absolute; top: 0; height: 46px; width: 298px; }
  .photo-office { left: 131px; background: linear-gradient(180deg, #4a3d30, var(--photo-a)); }
  .photo-timber { left: 454px; background: linear-gradient(180deg, #ecdcc8, var(--photo-b)); }
  .photo-floor { left: 776px; background: linear-gradient(180deg, #63666c, var(--photo-c)); }

  .btn { position: absolute; background: var(--button); color: #fff; font-family: "Raleway", sans-serif;
         font-weight: 700; font-size: 9px; letter-spacing: 1.6px; text-transform: uppercase;
         display: flex; align-items: center; justify-content: center; border: none; }
  .btn-load { left: 531px; top: 94px; width: 138px; height: 40px; }

  .section-title { position: absolute; left: 0; width: 1200px; top: 222px; text-align: center;
                   font-weight: 300; font-size: 32px; color: #333; letter-spacing: 0.3px; }
  .section-lead { position: absolute; left: 0; width: 1203px; top: 274px; text-align: center;
                  font-weight: 400; font-size: 12px; color: var(--muted); }

  .location-map { position: absolute; left: 132px; top: 335px; width: 936px; height: 368px;
                  background: linear-gradient(135deg, var(--map-base), var(--map-edge)); }
  .map-pin { position: absolute; left: 583px; top: 432px; width: 55px; height: 74px; }

  .field { position: absolute; border: 1px solid var(--field-line); background: #fff;
           font-family: "Raleway", sans-serif; font-size: 13.5px; color: #333; padding: 0 19px; }
  .field-name { left: 163px; top: 752px; width: 305px; height: 42px; line-height: 40px; }
  .field-email { left: 490px; top: 752px; width: 306px; height: 42px; line-height: 40px; }
  .field-message { left: 163px; top: 813px; width: 633px; height: 147px; padding-top: 13px; }
  .btn-send { left: 410px; top: 977px; width: 137px; height: 40px; }

  .address { position: absolute; left: 835px; top: 762px; color: var(--ink-soft); }
  .address h3 { font-weight: 500; font-size: 19px; margin-bottom: 19px; }
  .address p { font-weight: 300; font-size: 15px; line-height: 20px; }
  .address .phone { margin-top: 4px; }

  .site-footer { position: absolute; left: 0; top: 1065px; width: 1200px; height: 135px; background: var(--footer); color: var(--footer-ink); }
  .social { position: absolute; top: 42px; left: 0; width: 1200px; display: flex; justify-content: center; gap: 26px;
            font-weight: 500; font-size: 15px; }
  .copyright { position: absolute; top: 80px; left: 0; width: 1182px; text-align: center; font-weight: 300; font-size: 15px; }
</style>
</head>
<body>
  <section class="portfolio-band">
    <div class="portfolio-photo photo-office" role="img" aria-label="Fitout project photo: office floor with chair"></div>
    <div class="portfolio-photo photo-timber" role="img" aria-label="Fitout project photo: timber surface"></div>
    <div class="portfolio-photo photo-floor" role="img" aria-label="Fitout project photo: carpeted office floor"></div>
    <div class="btn btn-load">Load More</div>
  </section>

  <h2 class="section-title">CONTACT US</h2>
  <p class="section-lead">Neque porro quisquam est qui dolorem ipsum quia dolor sit amet, consectetur, adipisci velit...</p>

  <div class="location-map" role="img" aria-label="Street map showing the office location"></div>
  <svg class="map-pin" viewBox="0 0 55 74" aria-hidden="true">
    <path d="M27.5 0C12.3 0 0 12 0 27c0 18 27.5 47 27.5 47S55 45 55 27C55 12 42.7 0 27.5 0z" fill="var(--pin)"/>
    <circle cx="27.5" cy="27" r="10" fill="#fff"/>
  </svg>

  <div class="field field-name">Your Name</div>
  <div class="field field-email">Your Email</div>
  <div class="field field-message">Your Message</div>
  <div class="btn btn-send">Send</div>

  <address class="address" style="font-style: normal;">
    <h3>Our Address</h3>
    <p>24 Harlow Lane<br>Marden Vale, QLD 4102<br>Australia</p>
    <p class="phone">+61 7 3555 0148</p>
    <p class="phone">+61 7 3555 0148 |</p>
    <p class="phone">&nbsp;hello@tallowbridge.example</p>
  </address>

  <footer class="site-footer">
    <div class="social"><span>Social</span><span>Updates</span><span>Network</span></div>
    <p class="copyright">© 2016 Tallow Bridge (QLD) Pty Ltd All Rights Reserved</p>
  </footer>
</body>
</html>
```